Meridian Sound Wellness LLC Card Design

Need business card with a logo for a hearing aid sales and audiology business. We have two Hearing Instrument Specialists and one Audiologist on staff. Over 25 years in business. Locally owned and operated. Financing available. Most insurances accepted.

Meridian Sound Wellness LLC
48730 W Linden Row, Suite 9
Spokane, WA 99481
509-617-2085
www.meridiansoundnorth.example

Manager
Tobias Wrenfield HIS COHC
License #81729046

Target Market(s)

50yr old + people with a hearing loss.

Industry/Entity Type

Business

Contact Information for Business Card

48730 W Linden Row, Suite 9
Spokane, WA 99481
509-617-2085
www.meridiansoundnorth.example

Manager
Tobias Wrenfield HIS COHC
NRPL #81729046

Font styles to use
Serif
Sans Serif

Requirements
Must have
• Business name, Tobias's name and title(s) and contact information, License #, web address
Nice to have
Should not have

```html
<!DOCTYPE html>
<html lang="en">
<head>
<meta charset="utf-8">
<title>Meridian Sound Wellness LLC – Business Cards</title>
<link href="https://fonts.googleapis.com/css2?family=Bebas+Neue&family=Tenor+Sans&display=swap" rel="stylesheet">
<style>
  :root {
    --page-bg: #1d1e21;
    --card-bg: #ffffff;
    --ink: #161616;
    --skin-light: #e9b79a;
    --skin-dark: #a88a72;
    --magenta: #b51f6a;
    --green: #12a54a;
  }
  * { margin: 0; padding: 0; box-sizing: border-box; }
  html, body { width: 1200px; height: 1200px; overflow: hidden; }
  body {
    background: var(--page-bg);
    position: relative;
    font-family: "Tenor Sans", sans-serif;
  }
  .card {
    position: absolute;
    left: 100px;
    width: 1000px;
    height: 540px;
    background: var(--card-bg);
    border-radius: 26px;
    overflow: hidden;
  }
  .card--magenta { top: 45px; --accent: var(--magenta); }
  .card--green { top: 615px; --accent: var(--green); }

  .card__photo { position: absolute; left: 0; top: 0; width: 1000px; height: 470px; }

  .card__stripes { position: absolute; left: 0; bottom: 0; width: 100%; height: 70px; }
  .stripe { position: absolute; left: 0; width: 100%; background: var(--accent); }
  .stripe--thin-1 { top: 0; height: 8px; }
  .stripe--thin-2 { top: 15px; height: 8px; }
  .stripe--band { top: 30px; height: 40px; }

  .brand {
    position: absolute;
    right: 80px;
    top: 38px;
    text-align: right;
    font-family: "Bebas Neue", sans-serif;
    line-height: 0.95;
  }
  .brand__accent { display: block; font-size: 50px; color: var(--accent); }
  .brand__rest { display: block; font-size: 56px; color: var(--ink); }

  .person {
    position: absolute;
    right: 80px;
    top: 168px;
    text-align: right;
  }
  .person__name { font-size: 32px; color: var(--accent); letter-spacing: 0.5px; }
  .person__name .credentials { color: var(--ink); }
  .person__role { font-size: 25px; color: var(--accent); margin-top: 8px; }
  .person__license { font-size: 25px; color: var(--accent); margin-top: 6px; }
  .person__license .number { color: var(--ink); }

  .marker { position: absolute; right: 55px; top: 214px; width: 30px; height: 110px; }

  .contact {
    position: absolute;
    left: 420px;
    top: 330px;
    font-size: 21px;
    line-height: 34px;
    color: var(--ink);
  }
</style>
</head>
<body>

  <article class="card card--magenta">
    <svg class="card__photo" viewBox="0 0 1000 470" role="img" aria-label="Close-up photograph of a human ear">
      <defs>
        <linearGradient id="skin-magenta" x1="0" y1="0" x2="1" y2="1">
          <stop offset="0" stop-color="#e9b79a"/>
          <stop offset="0.75" stop-color="#d6a686"/>
          <stop offset="1" stop-color="#a88a72"/>
        </linearGradient>
      </defs>
      <polygon points="0,0 530,0 330,470 0,470" fill="url(#skin-magenta)"/>
    </svg>
    <div class="brand">
      <span class="brand__accent">Meridian</span>
      <span class="brand__rest">Sound Wellness LLC</span>
    </div>
    <div class="person">
      <p class="person__name">TOBIAS WRENFIELD <span class="credentials">HIS COHC</span></p>
      <p class="person__role">Manager</p>
      <p class="person__license">NRPL #<span class="number">81729046</span></p>
    </div>
    <svg class="marker" viewBox="0 0 30 110" aria-hidden="true">
      <rect x="22" y="0" width="6" height="110" fill="var(--accent)"/>
      <polygon points="0,80 28,80 28,104" fill="var(--accent)"/>
    </svg>
    <div class="contact">
      <p>Adress: 48730 W Linden Row, Suite 9</p>
      <p>Spokane, WA 99481</p>
      <p>Phone: 509-617-2085</p>
      <p>Web: www.meridiansoundnorth.example</p>
    </div>
    <div class="card__stripes">
      <div class="stripe stripe--thin-1"></div>
      <div class="stripe stripe--thin-2"></div>
      <div class="stripe stripe--band"></div>
    </div>
  </article>

  <article class="card card--green">
    <svg class="card__photo" viewBox="0 0 1000 470" role="img" aria-label="Close-up photograph of a human ear">
      <defs>
        <linearGradient id="skin-green" x1="0" y1="0" x2="1" y2="1">
          <stop offset="0" stop-color="#e9b79a"/>
          <stop offset="0.75" stop-color="#d6a686"/>
          <stop offset="1" stop-color="#a88a72"/>
        </linearGradient>
      </defs>
      <polygon points="0,0 530,0 330,470 0,470" fill="url(#skin-green)"/>
    </svg>
    <div class="brand">
      <span class="brand__accent">Meridian</span>
      <span class="brand__rest">Sound Wellness LLC</span>
    </div>
    <div class="person">
      <p class="person__name">TOBIAS WRENFIELD <span class="credentials">HIS COHC</span></p>
      <p class="person__role">Manager</p>
      <p class="person__license">NRPL #<span class="number">81729046</span></p>
    </div>
    <svg class="marker" viewBox="0 0 30 110" aria-hidden="true">
      <rect x="22" y="0" width="6" height="110" fill="var(--accent)"/>
      <polygon points="0,80 28,80 28,104" fill="var(--accent)"/>
    </svg>
    <div class="contact">
      <p>Adress: 48730 W Linden Row, Suite 9</p>
      <p>Spokane, WA 99481</p>
      <p>Phone: 509-617-2085</p>
      <p>Web: www.meridiansoundnorth.example</p>
    </div>
    <div class="card__stripes">
      <div class="stripe stripe--thin-1"></div>
      <div class="stripe stripe--thin-2"></div>
      <div class="stripe stripe--band"></div>
    </div>
  </article>

</body>
</html>
```